Brochure Design Project for Brockwell and Daughter Lumber

We are after an executive high-end trifold brochure to be sent to new customers. Please refer to document attached ('brochure notes') for the details.

Target Market(s)

Renovators, Wives, Architects, Builders

Requirements
Must have
• Back of brochure must have a map and contact details.

Must relate to the feel of our website ... brockwellanddaughterlumber.net

Nice to have
• A unique design - something unlike regular brochures.

Developed using Adobe Photoshop or InDesign

```html
<!DOCTYPE html>
<html lang="en">
<head>
<meta charset="utf-8">
<title>Brockwell and Daughter Lumber – Trifold Brochure</title>
<link rel="stylesheet" href="https://fonts.googleapis.com/css2?family=Arvo&family=PT+Sans:wght@400;700&display=swap">
<style>
  :root {
    --bark: #35322a;
    --bark-box: #3a362c;
    --forest-dark: #1f3a18;
    --forest-mid: #3f6d2a;
    --forest-light: #7fae52;
    --leaf: #8cb866;
    --cream: #f1efe6;
    --frame: #d9d3be;
    --frame-grey: #c4c6c6;
    --page: #ffffff;
  }
  * { box-sizing: border-box; margin: 0; padding: 0; }
  html, body { width: 1200px; height: 1086px; overflow: hidden; background: var(--page); }
  body { position: relative; font-family: "PT Sans", sans-serif; color: var(--cream); }

  .spread { position: absolute; left: 16px; width: 727px; }
  .spread--outside { top: 16px; height: 514px; background: var(--bark); }
  .spread--inside { top: 554px; height: 511px; background: var(--frame-grey); }

  .forest-photo {
    position: absolute; left: 0; top: 0; width: 727px; height: 389px;
    background: radial-gradient(ellipse at 50% 40%, var(--forest-light) 0%, var(--forest-mid) 45%, var(--forest-dark) 100%);
  }
  .side-panel { position: absolute; top: 0; height: 389px; background: rgba(45, 42, 34, 0.82); padding: 26px 22px; font-size: 9.6px; line-height: 1.16; }
  .side-panel--about { left: 0; width: 181px; }
  .side-panel--offer { left: 544px; width: 183px; padding-left: 24px; }
  .side-panel h2 { font-weight: 400; font-size: 11px; margin-bottom: 2px; }
  .side-panel p + p { margin-top: 10px; }
  .offer-point { font-size: 11.2px; margin-top: 12px; line-height: 1.1; }

  .tagline { position: absolute; left: 205px; top: 272px; width: 305px; text-align: center; font-size: 11.3px; line-height: 1.22; text-shadow: 0 0 3px rgba(0,0,0,0.5); }

  .cta { position: absolute; left: 10px; top: 408px; width: 182px; text-align: center; font-family: "Arvo", serif; line-height: 1.05; }
  .cta .small { font-size: 13px; }
  .cta .big { font-size: 18.5px; }

  .brand-name { position: absolute; font-family: "PT Sans", sans-serif; font-weight: 700; color: var(--leaf); text-align: center; line-height: 1.05; }
  .brand-name--outside { left: 212px; top: 430px; width: 118px; font-size: 17px; }
  .brand-name--inside { left: 0; top: 17px; width: 727px; font-size: 17px; }

  .contact { position: absolute; left: 333px; top: 430px; font-size: 9.4px; line-height: 1.1; }
  .contact .address { margin-bottom: 7px; }
  .contact dl { display: grid; grid-template-columns: 32px auto; }
  .contact dt::after { content: ""; }
  .map { position: absolute; left: 556px; top: 382px; width: 159px; height: 122px; background: linear-gradient(135deg, #e9e7df, #d8d6cc); border: 2px solid #e8e8e8; }

  .inner-frame { position: absolute; left: 4px; top: 4px; width: 719px; height: 448px; background: var(--frame); }
  .photo { position: absolute; }
  .photo--deck { left: 7px; top: 6px; width: 181px; height: 214px; background: linear-gradient(180deg, #5f87a8 0%, #8aa3a4 40%, #b08370 70%, #9c6b58 100%); }
  .photo--hardwood { left: 550px; top: 6px; width: 169px; height: 214px; background: linear-gradient(160deg, #5a2d1c 0%, #8a4a2c 45%, #e8e1d6 70%, #7a3e24 100%); }
  .photo--fence { left: 7px; top: 234px; width: 167px; height: 214px; background: linear-gradient(180deg, #9a9fa2 0%, #9e553a 35%, #a65a3c 75%, #bfbcb5 100%); }
  .photo--floor { left: 550px; top: 234px; width: 169px; height: 214px; background: linear-gradient(180deg, #e8e8e4 0%, #dcd8d0 45%, #c7893f 75%, #b0702c 100%); }

  .product { position: absolute; left: 189px; width: 349px; background: var(--bark-box); text-align: center; font-size: 8.3px; line-height: 1.2; padding: 8px 18px 0; }
  .product h3 { font-family: "Arvo", serif; font-weight: 400; font-size: 12.5px; margin-bottom: 3px; letter-spacing: 0.2px; }
  .product p + p { margin-top: 8px; }
  .product .strong { font-weight: 700; }
  .product--composite { top: 6px; height: 99px; }
  .product--kellan { top: 120px; height: 100px; }
  .product--fencing { top: 234px; height: 99px; padding-top: 24px; }
  .product--flooring { top: 347px; height: 101px; }
  .benefits { margin-top: 8px; }

  .inside-band { position: absolute; left: 0; top: 456px; width: 727px; height: 55px; background: var(--bark); }
</style>
</head>
<body>

<section class="spread spread--outside" aria-label="Brochure outside">
  <div class="forest-photo" role="img" aria-label="Photo of a sunlit green forest with tall tree trunks"></div>

  <div class="side-panel side-panel--about">
    <h2>About Us</h2>
    <p>Welcome to Brockwell and Daughter Lumber, from the family that brought you Greywood Timbers. We understand that deciding on the perfect project for home comes with lots of questions. We're the experts not only in timber, but design, engineering and construction. Be it a little fence or the largest house, our friendly team is here to help.</p>
    <p>We invite you to take your time looking over our website. We hope you find some inspiration to create your own masterpiece at your place. Don't forget we're only a phone call away and we're more than happy to assist.</p>
  </div>

  <div class="side-panel side-panel--offer">
    <h2>Want Cash?</h2>
    <p>Become a renovation star! If you allow us to take photos, video or leave a sign, we will reward you with $50 cash for every order taken from interest in your home improvement.</p>
    <p class="offer-point">We can come to you for free measure and quote.</p>
    <p class="offer-point">Design advise</p>
    <p class="offer-point">Can organize full installation</p>
    <p class="offer-point">Feel free to use any info or pictures from our website</p>
  </div>

  <p class="tagline">We are modern timber suppliers specializing in decks, hardwood floors and external cladding. We provide high end service to builders, DIY and tradesmen.</p>

  <div class="cta">
    <div class="small">Looking for something</div>
    <div class="big">different</div>
    <div class="small">or</div>
    <div class="big">unique?</div>
  </div>

  <div class="brand-name brand-name--outside">Brockwell &amp; Daughter</div>

  <div class="contact">
    <p class="address">Unit 7 / 12 Harlow Street<br>MARLEY HEIGHTS 4209</p>
    <dl>
      <dt>Call</dt><dd>: 1300 555 014 | (07) 5550 1834</dd>
      <dt>Fax</dt><dd>: (07) 5550 1835</dd>
      <dt>Email</dt><dd>: info@brockwellanddaughterlumber.com.au</dd>
      <dt>Web</dt><dd>: http://brockwellanddaughterlumber.net</dd>
    </dl>
  </div>

  <div class="map" role="img" aria-label="Street map showing the showroom location"></div>
</section>

<section class="spread spread--inside" aria-label="Brochure inside">
  <div class="inner-frame">
    <div class="photo photo--deck" role="img" aria-label="Photo of a composite timber deck beside the water"></div>
    <div class="photo photo--hardwood" role="img" aria-label="Photo of a dark hardwood deck with a round rug"></div>
    <div class="photo photo--fence" role="img" aria-label="Photo of a horizontal slat feature fence"></div>
    <div class="photo photo--floor" role="img" aria-label="Photo of a bright kitchen with timber flooring"></div>

    <article class="product product--composite">
      <h3>COMPOSITE TIMBER</h3>
      <p>Timber decks and screening are very popular but require constant maintenance. This timber-like product gives the look of timber, but with minimal upkeep.</p>
      <p class="strong">The 'greenest of green' … This timber-like product will give you the look you're after, without needing to oil …. EVER!</p>
    </article>

    <article class="product product--kellan">
      <h3>KELLAN TIMBER</h3>
      <p>The products include decking, flooring, structural timber and step treads.</p>
      <p class="benefits"><span class="strong">Benefits of the Kellan Timber species:</span><br>
      Durability Class 1 - no need to treat with nasty chemicals<br>
      Environmentally sustainable - fully certified<br>
      Strong | Beautiful<br>
      Wide range of uses available - decking, step treads, posts, joists.</p>
    </article>

    <article class="product product--fencing">
      <h3>FEATURE FENCING</h3>
      <p>We are able to supply you with designer fencing fully installed for much less than you think. Endless combinations available.<br>Call for an obligation-free quote today.</p>
    </article>

    <article class="product product--flooring">
      <h3>TRADITIONAL TIMBER AND BAMBOO FLOORING</h3>
      <p>Bamboo flooring is becoming an increasingly popular choice for many homeowners, architects, builders and interior designers who are looking for an environmental alternative to timber flooring that is a stylish, hard wearing, pre-finished flooring system.</p>
    </article>
  </div>

  <div class="inside-band">
    <div class="brand-name brand-name--inside">Brockwell &amp; Daughter</div>
  </div>
</section>

</body>
</html>
```